The Lanterns' Ledger - YouTube Channel Intro, Background, Title Graphic and Logo

I would like the following for a new YouTube channel. (1) An intro in which an animated quill pen writes on a background that looks like old parchment paper the name of the channel (The Lanterns' Ledger) in a Gothic style (like 'We the People' in the Constitution) (see https://www.vidplaza.example/watch?v=qKm3RtZpLxa for something similar); (2) a background that can replace my green screen in the videos (probably the same background as in the intro); (3) a lower-third title graphic for the videos and (4) a small logo for the lower right video corner, comprised of the acronym "TLL" in the font of the intro.
Updates

I really like the designs I have seen so far, but hope to see other ideas. I especially would like if someone tries to animate a quill pen for this. Thanks for your participation!

Target Market(s)

Viewers of political talking head videos on the left or the right

Font styles to use
Other font styles liked:
• Something the makes sense with the calligraphy in the intro

Requirements
Must have
• I love the animation referenced the description. Anything close to that would be fantastic.
Nice to have
• Lots of cool parchment images for background ideas in: https://texturebarn.example/aged-paper-samples/

```html
<!DOCTYPE html>
<html lang="en">
<head>
<meta charset="utf-8">
<title>The Lanterns' Ledger — Title Card</title>
<link rel="stylesheet" href="https://fonts.googleapis.com/css2?family=Allura&display=swap">
<style>
  :root {
    --parchment-light: #f1e9d4;
    --parchment-mid: #ddcba4;
    --parchment-edge: #a88d5f;
    --parchment-burn: #6e5a3a;
    --stain: rgba(150, 118, 70, 0.35);
    --ink: #1d1915;
  }

  * { margin: 0; padding: 0; box-sizing: border-box; }

  html, body {
    width: 1200px;
    height: 675px;
    overflow: hidden;
    background: var(--parchment-mid);
  }

  .title-card {
    position: relative;
    width: 1200px;
    height: 675px;
    overflow: hidden;
    background:
      radial-gradient(ellipse 4% 3% at 37% 78%, var(--stain), transparent 100%),
      radial-gradient(ellipse 2% 1.5% at 46% 84%, var(--stain), transparent 100%),
      radial-gradient(ellipse 3% 2% at 88% 22%, rgba(150,118,70,0.18), transparent 100%),
      radial-gradient(ellipse 70% 65% at 50% 48%, var(--parchment-light) 0%, var(--parchment-mid) 55%, var(--parchment-edge) 88%, var(--parchment-burn) 115%);
  }

  .title-card::after {
    content: "";
    position: absolute;
    inset: 0;
    box-shadow: inset 0 0 90px rgba(80, 60, 30, 0.45);
    pointer-events: none;
  }

  .channel-name {
    position: absolute;
    left: 0;
    right: 0;
    top: 50%;
    transform: translateY(-55%);
    text-align: center;
    font-family: "Allura", cursive;
    font-weight: 400;
    font-size: 104px;
    line-height: 1;
    letter-spacing: 1px;
    color: var(--ink);
  }
</style>
</head>
<body>
  <main class="title-card">
    <h1 class="channel-name">The Lanterns' Ledger</h1>
  </main>
</body>
</html>
```